WordPress Site Design and Code for Technology Consulting Startup

We need a WordPress design and code to a new site on Nimbo Vault. We have the logo and colors ready. The site will be a brochure site with a CONTACT page that contains a form that the prospective client fills out. The other pages would be ABOUT / SERVICES (3 option drop-down) / SUPPORT. The site should be appropriate for an IT Consulting / IT Managed Services / IT Project Management services in the Chicago area.

Target Market(s)

Across small, medium, large businesses.

Industry/Entity Type

Technology, network infrastructure, IT.

Coding

Coded - Design and coding required

Number of Pages Required

5+ page

Requirements
Nice to have
• I prefer mid-modern / simple / art deco / minimalist.

```html
<!DOCTYPE html>
<html lang="en">
<head>
<meta charset="utf-8">
<title>Corvane — IT Consulting in the Chicago Area</title>
<link href="https://fonts.googleapis.com/css2?family=Krona+One&family=Outfit:wght@300;400;500;600;700&display=swap" rel="stylesheet">
<style>
:root{
  --teal:#0a8fa8;
  --teal-dark:#087a90;
  --orange:#f57a10;
  --ink:#1b1b1b;
  --text:#333;
  --muted:#9a9a9a;
  --line:#d9d9d9;
  --soft:#f6f6f7;
  --white:#fff;
}
*{box-sizing:border-box;margin:0;padding:0}
html,body{width:1200px;height:3286px;overflow:hidden}
body{position:relative;font-family:"Outfit",sans-serif;color:var(--text);background:var(--white)}
.abs{position:absolute}
.eyebrow{color:var(--orange);font-weight:600;font-size:14px;text-align:center;letter-spacing:.5px}
.section-title{font-family:"Krona One",sans-serif;color:var(--teal);font-size:31px;text-align:center}
.rule{width:46px;height:2px;background:var(--teal)}
.btn{display:flex;align-items:center;justify-content:center;background:var(--orange);color:var(--white);font-weight:600;font-size:14px}

/* header */
.brand{display:flex;align-items:center;gap:8px;font-weight:700;font-size:24px;color:var(--teal);letter-spacing:1px}
.brand-mark{width:26px;height:26px;background:var(--orange)}
.nav{display:flex;gap:44px;font-size:11px;color:#333;letter-spacing:.3px}
.nav-contact{border:1px solid var(--orange);color:var(--orange);font-weight:600;font-size:11px;width:118px;height:34px;display:flex;align-items:center;justify-content:center}

/* hero */
.hero-photo{left:0;top:0;width:1200px;height:702px;background:linear-gradient(90deg,#b89a86 0%,#e9e6e2 35%,#f2f1ee 60%,#dcdad6 100%)}
.hero-fade{left:0;top:0;width:1200px;height:330px;background:linear-gradient(180deg,rgba(255,255,255,.92) 0%,rgba(255,255,255,.75) 70%,rgba(255,255,255,0) 100%)}
.hero-kicker{top:123px;width:1200px;text-align:center;color:var(--teal);font-weight:700;font-size:14px;letter-spacing:4px}
.hero-title{top:148px;width:1200px;text-align:center;font-family:"Krona One",sans-serif;color:#1b1b1b;font-size:26px;line-height:38px;font-weight:400}
.scroll-dot{left:580px;top:633px;width:42px;height:42px;border-radius:50%;background:var(--white);box-shadow:0 2px 8px rgba(0,0,0,.15);display:flex;align-items:center;justify-content:center}

/* services */
.card{width:271px;height:274px;background:var(--white);box-shadow:0 4px 24px rgba(0,0,0,.06);text-align:center}
.card-icon{margin:36px auto 0;width:98px;height:98px;border-radius:50%;border:1px solid #ddd;background:#fafafa;display:flex;align-items:center;justify-content:center}
.card-icon.active{background:var(--orange);border-color:var(--orange)}
.card h3{font-family:"Krona One",sans-serif;font-size:14px;color:var(--ink);margin-top:26px;font-weight:400}
.card p{font-size:13px;line-height:21px;margin:12px 22px 0}

/* about */
.about-photo{left:161px;top:1234px;width:432px;height:416px;border-radius:0 20px 0 0;background:linear-gradient(135deg,#cfd7e0 0%,#9aa9ba 55%,#5c6b7d 100%)}
.about-copy{left:641px;top:1254px;width:395px}
.about-copy .eyebrow{text-align:left}
.about-copy h2{font-family:"Krona One",sans-serif;color:var(--teal);font-size:30px;margin-top:6px;font-weight:400}
.about-copy .lead{font-weight:600;color:var(--ink);font-size:13px;line-height:19px;margin-top:26px}
.about-copy p{font-size:12.5px;line-height:24.5px;margin-top:12px}

/* testimonial */
.arrow-btn{width:38px;height:36px;border:1px solid #e3e3e3;border-radius:4px;background:#f7f7f7;display:flex;align-items:center;justify-content:center}
.quote-text{left:215px;top:2064px;width:770px;text-align:center;font-style:italic;font-size:13px;line-height:25px}
.client-name{top:2146px;width:1200px;text-align:center;font-family:"Krona One",sans-serif;color:var(--teal);font-size:14px}
.client-org{top:2171px;width:1200px;text-align:center;font-style:italic;font-size:12px;color:#bbb}

/* quote form */
.quote-box{left:232px;top:2272px;width:735px;height:510px;background:var(--white);box-shadow:0 6px 30px rgba(0,0,0,.06)}
.quote-box h2{position:absolute;top:62px;width:100%;text-align:center;color:var(--teal);font-size:30px;font-weight:500}
.quote-box .rule{position:absolute;left:344px;top:111px}
.quote-intro{position:absolute;top:139px;left:72px;width:591px;text-align:center;font-size:12.5px;line-height:22px}
.field{position:absolute;border:1px solid var(--line);font-size:11px;color:#888;padding:12px 15px;background:transparent}
.corner{position:absolute;right:0;bottom:0}

/* footer */
.footer{left:0;top:2873px;width:1200px;height:369px;background:var(--teal);color:var(--white)}
.footer h4{font-size:16px;font-weight:500}
.footer .rule{background:var(--white);width:34px;margin-top:10px}
.footer ul{list-style:none;font-size:13px;line-height:30px;margin-top:14px}
.contact-item{display:flex;gap:12px;font-size:12.5px;line-height:20px;margin-top:12px}
.social{display:flex;align-items:center;gap:9px;font-size:13px;margin-top:12px}
.social i{width:30px;height:30px;border:1px solid var(--white);border-radius:50%;display:block}
.footer-brand{left:838px;top:145px;width:202px;text-align:center;font-weight:700;font-size:32px;letter-spacing:2px}
.footer-brand span{display:block;width:50px;height:50px;border:3px solid var(--white);margin:0 auto 10px}
.copyright{left:0;top:3242px;width:1200px;height:44px;background:var(--orange);color:var(--white);font-size:12px;display:flex;align-items:center;justify-content:center}
</style>
</head>
<body>

<!-- Hero -->
<div class="abs hero-photo" role="img" aria-label="Photo of a busy open-plan office with people working at desks"></div>
<div class="abs hero-fade"></div>
<svg class="abs" style="left:0;top:600px" width="1200" height="110" viewBox="0 0 1200 110">
  <polygon points="0,102 0,110 1200,110 1200,0 338,86" fill="#fff"/>
  <polygon points="338,86 1200,0 1200,22 338,88" fill="#9aa0a6" opacity=".6"/>
  <polygon points="650,102 1200,40 1200,102" fill="var(--teal)"/>
  <polygon points="338,88 1200,22 1200,40 338,100" fill="#c9cdd0"/>
</svg>

<header>
  <div class="abs brand" style="left:161px;top:22px"><span class="brand-mark"></span>CORVANE</div>
  <nav class="abs nav" style="left:556px;top:36px">
    <span>HOME</span><span>ABOUT</span><span>SERVICES &#8964;</span><span>SUPPORT</span>
  </nav>
  <div class="abs nav-contact" style="left:921px;top:24px">CONTACT &rarr;</div>
</header>

<div class="abs hero-kicker">WE PROVIDE</div>
<h1 class="abs hero-title">IT CONSULTING / IT MANAGED SERVICES /<br>IT PROJECT MANAGEMENT SERVICES IN<br>THE CHICAGO AREA</h1>
<div class="abs btn" style="left:528px;top:272px;width:144px;height:41px">CONTACT &rarr;</div>
<div class="abs scroll-dot">
  <svg width="12" height="8" viewBox="0 0 12 8"><path d="M1 1l5 5 5-5" fill="none" stroke="#333" stroke-width="1.6"/></svg>
</div>

<!-- Services -->
<section>
  <div class="abs eyebrow" style="top:764px;width:1200px">SERVICES</div>
  <h2 class="abs section-title" style="top:786px;width:1200px;font-weight:400">Best IT Solutions For You</h2>
  <div class="abs rule" style="left:577px;top:830px"></div>

  <div class="abs card" style="left:161px;top:869px">
    <div class="card-icon"><svg width="44" height="44"><circle cx="22" cy="22" r="16" fill="none" stroke="var(--teal)" stroke-width="2"/></svg></div>
    <h3>IT Consulting</h3>
    <p>Lorem ipsum dolor sit amet ectetuer adipiscing elit, sed diam nonummy nibh euismod</p>
  </div>
  <div class="abs card" style="left:465px;top:869px">
    <div class="card-icon active"><svg width="44" height="44"><rect x="6" y="8" width="32" height="24" fill="none" stroke="#fff" stroke-width="2"/></svg></div>
    <h3>IT Managed Services</h3>
    <p>Lorem ipsum dolor sit amet ectetuer adipiscing elit, sed diam nonummy nibh euismod</p>
  </div>
  <div class="abs card" style="left:768px;top:869px">
    <div class="card-icon"><svg width="44" height="44"><rect x="8" y="4" width="26" height="34" fill="none" stroke="var(--teal)" stroke-width="2"/><path d="M13 14l3 3 5-6M13 26l3 3 5-6" fill="none" stroke="var(--orange)" stroke-width="2"/></svg></div>
    <h3>IT Project Management</h3>
    <p>Lorem ipsum dolor sit amet ectetuer adipiscing elit, sed diam nonummy nibh euismod</p>
  </div>
</section>

<!-- About -->
<svg class="abs" style="left:0;top:1225px" width="1200" height="620" viewBox="0 0 1200 620">
  <path d="M0 40 Q600 -20 1200 40 L1200 620 Q600 470 0 620 Z" fill="var(--soft)"/>
</svg>
<section>
  <div class="abs about-photo" role="img" aria-label="Photo of two colleagues celebrating in front of a desktop computer"></div>
  <div class="abs about-copy">
    <div class="eyebrow">ABOUT</div>
    <h2>Corvane</h2>
    <div class="rule" style="margin-top:12px"></div>
    <p class="lead">Lorem ipsum dolor sit amet, consectetur adipiscing elit, sed do eiusmod tempor incididunt ut labore.</p>
    <p>Sed ut perspiciatis unde omnis iste natus error sit voluptatem accusantium doloremque laudantium, totam rem aperiam eaque ipsa quae ab illo inventore veritatis et quasi.</p>
    <p>At vero eos et accusamus et iusto odio dignissimos ducimus qui blanditiis praesentium voluptatum deleniti atque corrupti quos dolores et quas molestias excepturi sint Temporibus autem quibusdam et aut officiis debitis...</p>
    <div class="btn" style="width:128px;height:37px;margin-top:20px;font-size:13px">Read More</div>
  </div>
</section>

<!-- Testimonials -->
<section>
  <div class="abs eyebrow" style="top:1849px;width:1200px">TESTIMONIALS</div>
  <h2 class="abs section-title" style="top:1871px;width:1200px;font-weight:400">Trusted From Our Clients</h2>
  <div class="abs rule" style="left:577px;top:1914px"></div>
  <div class="abs" style="left:555px;top:1950px;width:90px;height:60px;border-radius:45px 45px 0 0;background:#f2f2f2"></div>
  <svg class="abs" style="left:572px;top:1950px" width="56" height="46" viewBox="0 0 56 46">
    <path d="M4 4h18v16c0 12-6 20-16 24l-2-6c6-3 8-8 8-14H4z M32 4h18v16c0 12-6 20-16 24l-2-6c6-3 8-8 8-14H32z" fill="var(--orange)"/>
  </svg>
  <div class="abs" style="top:2014px;width:1200px;text-align:center;font-weight:600;font-size:19px;color:var(--ink)">Brightlane</div>
  <div class="abs arrow-btn" style="left:102px;top:2050px"><svg width="8" height="12"><path d="M7 1L2 6l5 5" fill="none" stroke="var(--orange)" stroke-width="1.6"/></svg></div>
  <div class="abs arrow-btn" style="left:1061px;top:2050px"><svg width="8" height="12"><path d="M1 1l5 5-5 5" fill="none" stroke="var(--orange)" stroke-width="1.6"/></svg></div>
  <p class="abs quote-text">Lorem ipsum dolor sit amet, consectetuer adipiscing elit, sed diam nonummy nibh euismod tincidunt ut laoreet dolore magna aliquam erat volutpat. Ut wisi enim ad minim veniam, quis nostrud exerci tation ullamcorper suscipit lobortis nisl ut aliquip ex ea commodo consequat.</p>
  <div class="abs client-name">Dana Whitfield</div>
  <div class="abs client-org">Lumen Works</div>
</section>

<!-- Request a quote -->
<section class="abs quote-box">
  <h2>Request A Quote</h2>
  <div class="rule"></div>
  <p class="quote-intro">If you have any questions about Corvane and interested in speaking with us about adding services for your home or business, please get in touch with us using the information below:</p>
  <div class="field" style="left:68px;top:197px;width:292px;height:37px">Name</div>
  <div class="field" style="left:376px;top:197px;width:292px;height:37px">Email</div>
  <div class="field" style="left:68px;top:249px;width:292px;height:37px">Phone</div>
  <div class="field" style="left:376px;top:249px;width:292px;height:37px">Company</div>
  <div class="field" style="left:68px;top:302px;width:600px;height:90px">Message</div>
  <div class="btn" style="position:absolute;left:308px;top:414px;width:120px;height:37px;border-radius:2px;font-size:13px">Submit</div>
  <svg class="corner" width="38" height="38"><polygon points="38,0 38,38 0,38" fill="var(--orange)"/></svg>
</section>

<!-- Footer -->
<footer class="abs footer">
  <div class="abs" style="left:161px;top:82px">
    <h4>Quick Links</h4><div class="rule"></div>
    <ul><li>• Home</li><li>• About</li><li>• Services</li><li>• Support</li><li>• Contact</li></ul>
  </div>
  <div class="abs" style="left:353px;top:82px;width:220px">
    <h4>Contact Details</h4><div class="rule"></div>
    <div class="contact-item" style="margin-top:22px">
      <svg width="13" height="18" viewBox="0 0 13 18"><path d="M6.5 1a5.5 5.5 0 0 0-5.5 5.5C1 11 6.5 17 6.5 17S12 11 12 6.5A5.5 5.5 0 0 0 6.5 1z" fill="#fff"/><circle cx="6.5" cy="6.5" r="2" fill="var(--teal)"/></svg>
      <div><b style="font-weight:500">Address</b><br>123 Ut Wisi Enim Ad Minim<br>Veniam Quis Nostrud.</div>
    </div>
    <div class="contact-item" style="margin-top:16px">
      <svg width="13" height="14" viewBox="0 0 13 14"><path d="M3 1l2 3-1.5 1.5c.8 1.8 2.2 3.2 4 4L9 8l3 2-1.5 3C5 12 1 7.5 1 2.5z" fill="#fff"/></svg>
      <div><b style="font-weight:500">Phone</b><br>123 456 7890</div>
    </div>
    <div class="contact-item" style="margin-top:16px">
      <svg width="14" height="11" viewBox="0 0 14 11"><rect x="0.5" y="0.5" width="13" height="10" fill="none" stroke="#fff"/><path d="M1 1l6 5 6-5" fill="none" stroke="#fff"/></svg>
      <div><b style="font-weight:500">Email</b><br>inquiry@corvane.com</div>
    </div>
  </div>
  <div class="abs" style="left:644px;top:82px">
    <h4>Follow Us</h4><div class="rule"></div>
    <div class="social" style="margin-top:24px"><i></i>Chatterbox</div>
    <div class="social"><i></i>Streamly</div>
    <div class="social"><i></i>Snapfeed</div>
    <div class="social"><i></i>Buzzline</div>
  </div>
  <div class="abs footer-brand"><span></span>CORVANE</div>
</footer>
<div class="abs copyright">© 2023 Corvane Information Technology Consulting. All Rights Reserved.</div>

</body>
</html>
```